App Design for FlavorRoam

We need an app design for a new app called FlavorRoam, which is an app designed to inspire exploration through personalized recipe generation, local restaurant discoveries, and a vibrant community platform. It caters to food enthusiasts looking to explore global cuisines or find the best local dining spots, offering a premium experience with selected features available for free.

-------UPDATED-----
This app will be AI Driven and may not be heavily dependent on media (images,videos) at first, especially for the Recipe generator feature. Our goal is to still have attractive UI. The core functionalities we are looking are the following
1. Recipe Generator: Either user choose a specific cuisine(italian,spanish), or user inputs ingredients and get recipe, or get recipe for different occasions (xmas, thanksgiving ) and get a randomly get recipe to cook, plain simple. We expect the recipes to be displayed in clear and not too generic manner starting with ingredients and expected duration at top and then step by step guide. We also intend to enable premium users to have playful action button or icon to get unlimited recipes generated until they find what they like and also have save for later feature. These premium features should be disabled for free users and prompted to subscribe if they click them with nice popup
2. Restaurant Recommendation - will have selected pictures and will be based on inputs such as zip code and other filters such as cousine types. Premium users can filter by price range, get unlimited recommendation, see actual price range in the recommendation and can save for later where they can find it later. Free users cannot filter by price (disabled) and should see it hidden in the recommendation
3. Meal Planning - will include just simple and random meal plan with just one button or limited interaction for free, users need to subscribe to get features such as customized plan such as considering allergies or diet preferences. Premium users can also get a shopping checklist of ingredients for weekly meal preps and their step by step guide for each meal recipe.
2. Community Sharing: users can view posts and engage with community content
Updates

Hello Designers,

The initial price was not fair for the work. So I have increased it. There will also be $50-100 bonus for those who come up with great designs or for those who incorporate interesting stuff. Thank you! Much appreciated 🙏

Colors
0054AA
0677BA
7BADD7
CADEEF
E8F1F8
0094D4
00A9DD
6FCCEA
C7EBF8
E9F6FB
00AB8E
00BBA5
67D7C9
C6EFE9
E9F9F6
FFC000
F8CF3A
FAE287
FDF2CF
FEFAEE
F0912C
F2A743
F7CA91
FBE8D2
FDF5EE
EE7325
F08F49
F5BC92
FAE3D3
FDF4ED
A7469A
B969AE
D3A5CF
EDDBEB
F8F0F9
6B429C
8869AF
B7A5CE
E3DAEB
F3F0F8

```html
<!DOCTYPE html>
<html lang="en">
<head>
<meta charset="utf-8">
<title>FlavorRoam – App Screens</title>
<link href="https://fonts.googleapis.com/css2?family=Inter:wght@400;500;600;700&display=swap" rel="stylesheet">
<style>
:root{
  --orange:#F0912C;
  --orange-soft:#FBE8D2;
  --orange-pale:#FDF5EE;
  --yellow:#F8CF3A;
  --yellow-pale:#FDF2CF;
  --ink:#1c1c1c;
  --muted:#8a8a8a;
  --line:#e7e7e7;
  --field:#f4f4f4;
  --board:#404040;
  --page:#ffffff;
  --dim:#3b3b3b;
}
*{box-sizing:border-box;margin:0;padding:0}
html,body{width:1200px;height:952px;overflow:hidden;background:var(--page)}
body{font-family:"Inter",sans-serif;color:var(--ink)}
.stage{position:absolute;left:0;top:0;width:2156px;height:1710px;transform:scale(0.55659);transform-origin:0 0}
.section-tag{position:absolute;left:25px;top:3px;background:#3a3a3a;color:#fff;font-size:8px;padding:4px 4px;border-radius:2px}
.board{position:absolute;left:25px;top:25px;width:2106px;height:1660px;background:var(--board)}
.screen{position:absolute;width:233px;background:#fff;overflow:hidden}
.screen > *{position:absolute}
.status{left:12px;top:9px;width:209px;height:10px;display:flex;justify-content:space-between;align-items:center;font-size:8.5px;font-weight:600}
.back{left:14px;top:37px;display:flex;align-items:center;gap:7px;font-size:7.5px;color:#555}
.back i{width:18px;height:18px;background:#222;border-radius:4px;display:flex;align-items:center;justify-content:center}
.title{font-size:12.5px;font-weight:500}
.small{font-size:7.5px;color:var(--muted)}
.banner{left:12px;top:70px;width:208px;height:46px;background:var(--orange-soft);border-radius:6px}
.banner b{position:absolute;left:10px;top:12px;font-size:9.5px;font-weight:500}
.banner span{position:absolute;left:10px;top:27px;font-size:6.5px;color:var(--orange)}
.banner em{position:absolute;right:9px;top:10px;width:88px;height:26px;background:var(--orange);border-radius:4px;color:#fff;font-style:normal;font-size:8px;display:flex;align-items:center;justify-content:center;gap:5px}
.heading{left:0;width:233px;top:140px;text-align:center;font-size:12.5px;font-weight:500}
.tabs{left:12px;top:175px;width:209px;height:21px;border-bottom:1px solid var(--line);display:flex;font-size:8px;color:#666}
.tabs span{flex:1;text-align:center;padding-top:2px}
.tabs .on{color:var(--orange);border-bottom:2px solid var(--orange)}
.field{height:26px;border:1px solid var(--line);background:#fafafa;border-radius:5px;font-size:6.5px;color:#aaa;display:flex;align-items:center;padding-left:10px}
.add{height:26px;width:50px;background:var(--orange);color:#fff;border-radius:5px;font-size:8px;display:flex;align-items:center;justify-content:center}
.chips{display:flex;flex-wrap:wrap;gap:9px 6px;width:209px}
.chip{height:22px;border:1px solid var(--line);border-radius:12px;padding:0 10px;font-size:8px;color:#777;display:flex;align-items:center;gap:5px}
.chip.x::after{content:"";width:7px;height:7px;border:1px solid var(--orange);border-radius:50%;background:radial-gradient(var(--orange) 25%,transparent 30%)}
.chip.on{border-color:var(--orange);color:var(--orange)}
.chip.fill{background:var(--orange);border-color:var(--orange);color:#fff;justify-content:center}
.subbar{left:0;width:233px;height:27px;background:#f6f6f6;font-size:7.5px;display:flex;align-items:center;justify-content:space-between;padding:0 12px 0 10px}
.cta{left:0;width:233px;height:37px;background:var(--orange);color:#fff;font-size:8px;font-weight:500;display:flex;align-items:center;justify-content:center}
.cta.off{background:#cfcfcf;color:#777}
.btn{height:27px;border-radius:4px;font-size:8px;display:flex;align-items:center;justify-content:center}
.btn.primary{background:var(--orange);color:#fff}
.btn.ghost{background:#f7f7f7;color:#bbb}
.btn.line{border:1px solid var(--line);color:#333;background:#fff}
.option{left:22px;width:188px;height:38px;border:1px solid var(--line);border-radius:5px;display:flex;align-items:center;padding:0 10px;gap:9px;font-size:8px}
.option .ic{width:13px;height:13px;background:var(--orange);border-radius:3px}
.option svg{margin-left:auto}
.cuisine{width:65px;height:73px;border:1px solid var(--line);border-radius:6px;font-size:7.5px;text-align:center}
.cuisine .dish{position:absolute;left:13px;top:7px;width:39px;height:39px;border-radius:50%}
.cuisine span{position:absolute;left:0;right:0;bottom:8px}
.cuisine.on{border-color:var(--orange)}
.label{font-size:8px;font-weight:600}
.para{font-size:7.6px;line-height:12.4px;color:#777;width:208px}
.rule{height:1px;background:var(--line);width:208px}
.list-item{font-size:7.6px;color:#888}
.dimmed{background:var(--dim)}
.sheet{left:0;width:233px;background:#fff;border-radius:18px 18px 0 0}
.closer{width:18px;height:18px;border-radius:50%;background:#fff;display:flex;align-items:center;justify-content:center}
.radio{display:flex;align-items:center;gap:6px;font-size:7.5px;color:#555}
.radio i{width:11px;height:11px;border-radius:50%;border:1px solid #ccc}
.radio i.on{border-color:var(--orange);background:radial-gradient(var(--orange) 40%,#fff 45%)}
.menu{left:12px;top:86px;display:flex;flex-direction:column;gap:19px;font-size:8px}
.menu div{display:flex;align-items:center;gap:9px;height:13px}
.track{height:2px;background:#f3c99a;width:208px}
.knob{width:22px;height:18px;background:var(--orange);border-radius:3px;color:#fff;font-size:6.5px;display:flex;align-items:center;justify-content:center}
</style>
</head>
<body>
<div class="stage">
  <div class="section-tag">Section 1</div>
  <div class="board"></div>

  <!-- Row 1 / Screen: welcome choices -->
  <section class="screen" style="left:179px;top:238px;height:504px">
    <div class="status"><span>9:41</span><svg width="44" height="8" viewBox="0 0 44 8"><rect x="0" y="5" width="2" height="3" fill="#111"/><rect x="3" y="3.5" width="2" height="4.5" fill="#111"/><rect x="6" y="2" width="2" height="6" fill="#111"/><rect x="9" y="0" width="2" height="8" fill="#111"/><path d="M16 3a6 6 0 0 1 9 0l-1 1a4.5 4.5 0 0 0-7 0zM18.5 5.5a2.5 2.5 0 0 1 4 0L20.5 8z" fill="#111"/><rect x="31" y="1" width="11" height="6" rx="1.5" fill="#111"/><rect x="42.5" y="3" width="1" height="2" fill="#111"/></svg></div>
    <div class="back"><i><svg width="6" height="8" viewBox="0 0 6 8"><path d="M4.5 1 1.5 4l3 3" stroke="#fff" stroke-width="1.4" fill="none"/></svg></i>Back</div>
    <div role="img" aria-label="Bowl of green salad seen from above" style="left:92px;top:77px;width:48px;height:48px;border-radius:50%;background:radial-gradient(circle,#8cbd3f 0,#4f8a2c 45%,#c8d0d2 62%,#8d9a9e 100%)"></div>
    <div style="left:0;width:233px;top:144px;text-align:center;font-size:12px">Hi User,</div>
    <div style="left:0;width:233px;top:164px;text-align:center;font-size:12.5px;font-weight:500">What’d you like today?</div>
    <div class="option" style="top:201px"><span class="ic"></span>Get a Recipe<svg width="6" height="9" viewBox="0 0 6 9"><path d="M1 1l3.5 3.5L1 8" stroke="#555" fill="none"/></svg></div>
    <div class="option" style="top:250px"><span class="ic"></span>Eat Out<svg width="6" height="9" viewBox="0 0 6 9"><path d="M1 1l3.5 3.5L1 8" stroke="#555" fill="none"/></svg></div>
    <div class="option" style="top:299px"><span class="ic"></span>Plan a Meal<svg width="6" height="9" viewBox="0 0 6 9"><path d="M1 1l3.5 3.5L1 8" stroke="#555" fill="none"/></svg></div>
  </section>

  <!-- Row 1 / Screen: add ingredients -->
  <section class="screen" style="left:433px;top:238px;height:504px">
    <div class="status"><span>9:41</span><svg width="44" height="8" viewBox="0 0 44 8"><rect x="0" y="5" width="2" height="3" fill="#111"/><rect x="3" y="3.5" width="2" height="4.5" fill="#111"/><rect x="6" y="2" width="2" height="6" fill="#111"/><rect x="9" y="0" width="2" height="8" fill="#111"/><path d="M16 3a6 6 0 0 1 9 0l-1 1a4.5 4.5 0 0 0-7 0zM18.5 5.5a2.5 2.5 0 0 1 4 0L20.5 8z" fill="#111"/><rect x="31" y="1" width="11" height="6" rx="1.5" fill="#111"/><rect x="42.5" y="3" width="1" height="2" fill="#111"/></svg></div>
    <div class="back"><i><svg width="6" height="8" viewBox="0 0 6 8"><path d="M4.5 1 1.5 4l3 3" stroke="#fff" stroke-width="1.4" fill="none"/></svg></i>Back</div>
    <div class="banner"><b>Generate Recipes</b><span>Lorem Ipsum is simply</span><em>✦ Surprise Me!</em></div>
    <div class="heading">Customise your recipe</div>
    <div class="tabs"><span class="on">Add Ingredients</span><span>Cousine</span><span>Occasion</span></div>
    <div class="field" style="left:12px;top:204px;width:155px">Enter ingredient name</div>
    <div class="add" style="left:170px;top:204px">Add +</div>
    <div class="chips" style="left:12px;top:244px"><span class="chip x">Beef</span><span class="chip x">Onion</span><span class="chip x">Tomatoes</span><span class="chip x">Garlic</span><span class="chip x">Chili</span></div>
    <div class="subbar" style="top:440px">Subscribe to add maximum cooking time<svg width="6" height="9" viewBox="0 0 6 9"><path d="M1 1l3.5 3.5L1 8" stroke="#555" fill="none"/></svg></div>
    <div class="cta off" style="top:467px">Get your recipe</div>
  </section>

  <!-- Row 1 / Screen: cuisine -->
  <section class="screen" style="left:687px;top:238px;height:648px">
    <div class="status"><span>9:41</span><svg width="44" height="8" viewBox="0 0 44 8"><rect x="0" y="5" width="2" height="3" fill="#111"/><rect x="3" y="3.5" width="2" height="4.5" fill="#111"/><rect x="6" y="2" width="2" height="6" fill="#111"/><rect x="9" y="0" width="2" height="8" fill="#111"/><path d="M16 3a6 6 0 0 1 9 0l-1 1a4.5 4.5 0 0 0-7 0zM18.5 5.5a2.5 2.5 0 0 1 4 0L20.5 8z" fill="#111"/><rect x="31" y="1" width="11" height="6" rx="1.5" fill="#111"/><rect x="42.5" y="3" width="1" height="2" fill="#111"/></svg></div>
    <div class="back"><i><svg width="6" height="8" viewBox="0 0 6 8"><path d="M4.5 1 1.5 4l3 3" stroke="#fff" stroke-width="1.4" fill="none"/></svg></i>Back</div>
    <div class="banner"><b>Generate Recipes</b><span>Lorem Ipsum is simply</span><em>✦ Surprise Me!</em></div>
    <div class="heading">Customise your recipe</div>
    <div class="tabs"><span>Add Ingredients</span><span class="on">Cousine</span><span>Occasion</span></div>
    <div class="cuisine" style="left:12px;top:211px"><div class="dish" role="img" aria-label="American pasta dish" style="background:radial-gradient(#e9a13b 30%,#c8361f 70%)"></div><span>American</span></div>
    <div class="cuisine" style="left:83px;top:211px"><div class="dish" role="img" aria-label="Italian pasta dish" style="background:radial-gradient(#d98c4a 30%,#bcd6ee 70%)"></div><span>Italian</span></div>
    <div class="cuisine on" style="left:154px;top:211px"><div class="dish" role="img" aria-label="Mexican dish" style="background:radial-gradient(#f0c04a 30%,#7a3a1c 75%)"></div><span>Mexican</span><svg style="position:absolute;right:3px;top:3px" width="10" height="10" viewBox="0 0 10 10"><circle cx="5" cy="5" r="5" fill="#F0912C"/><path d="M2.8 5.1l1.5 1.5 3-3" stroke="#fff" fill="none"/></svg></div>
    <div class="cuisine" style="left:12px;top:290px"><div class="dish" role="img" aria-label="Japanese sushi dish" style="background:radial-gradient(#f2f2f2 25%,#3fb3b8 60%)"></div><span>Japanese</span></div>
    <div class="cuisine" style="left:83px;top:290px"><div class="dish" role="img" aria-label="Chinese noodle dish" style="background:radial-gradient(#b9652c 30%,#4a2a18 75%)"></div><span>Chinese</span></div>
    <div class="cuisine" style="left:154px;top:290px"><div class="dish" role="img" aria-label="Indian rice dish" style="background:radial-gradient(#eee1c7 30%,#a6521f 75%)"></div><span>Indian</span></div>
    <div class="cuisine" style="left:12px;top:369px"><div class="dish" role="img" aria-label="African stew dish" style="background:radial-gradient(#d3582b 30%,#6a2a14 75%)"></div><span>African</span></div>
    <div class="cuisine" style="left:83px;top:369px"><div class="dish" role="img" aria-label="American pasta dish" style="background:radial-gradient(#e9a13b 30%,#c8361f 70%)"></div><span>American</span></div>
    <div class="cuisine" style="left:154px;top:369px"><div class="dish" role="img" aria-label="American pasta dish" style="background:radial-gradient(#e9a13b 30%,#c8361f 70%)"></div><span>American</span></div>
    <div style="left:12px;top:462px;font-size:9.5px;font-weight:500">Avoid Ingredients</div>
    <div class="field" style="left:12px;top:484px;width:155px">Enter ingredient name</div>
    <div class="add" style="left:170px;top:484px">Add +</div>
    <div class="chips" style="left:12px;top:524px"><span class="chip x">Beef</span><span class="chip x">Onion</span><span class="chip x">Tomatoes</span></div>
    <div class="subbar" style="top:584px">Subscribe to add maximum cooking time<svg width="6" height="9" viewBox="0 0 6 9"><path d="M1 1l3.5 3.5L1 8" stroke="#555" fill="none"/></svg></div>
    <div class="cta" style="top:611px">Get your recipe</div>
  </section>

  <!-- Row 1 / Screen: occasion -->
  <section class="screen" style="left:944px;top:238px;height:504px">
    <div class="status"><span>9:41</span><svg width="44" height="8" viewBox="0 0 44 8"><rect x="0" y="5" width="2" height="3" fill="#111"/><rect x="3" y="3.5" width="2" height="4.5" fill="#111"/><rect x="6" y="2" width="2" height="6" fill="#111"/><rect x="9" y="0" width="2" height="8" fill="#111"/><path d="M16 3a6 6 0 0 1 9 0l-1 1a4.5 4.5 0 0 0-7 0zM18.5 5.5a2.5 2.5 0 0 1 4 0L20.5 8z" fill="#111"/><rect x="31" y="1" width="11" height="6" rx="1.5" fill="#111"/><rect x="42.5" y="3" width="1" height="2" fill="#111"/></svg></div>
    <div class="back"><i><svg width="6" height="8" viewBox="0 0 6 8"><path d="M4.5 1 1.5 4l3 3" stroke="#fff" stroke-width="1.4" fill="none"/></svg></i>Back</div>
    <div class="banner"><b>Generate Recipes</b><span>Lorem Ipsum is simply</span><em>✦ Surprise Me!</em></div>
    <div class="heading">Customise your recipe</div>
    <div class="tabs"><span>Add Ingredients</span><span>Cousine</span><span class="on">Occasion</span></div>
    <div class="chips" style="left:12px;top:212px"><span class="chip">Christmas</span><span class="chip">Thanks Giving</span><span class="chip">Birthday</span><span class="chip">Marriage Anniversary</span><span class="chip">Week End</span></div>
    <div class="subbar" style="top:440px">Subscribe to add maximum cooking time<svg width="6" height="9" viewBox="0 0 6 9"><path d="M1 1l3.5 3.5L1 8" stroke="#555" fill="none"/></svg></div>
    <div class="cta" style="top:467px">Skip &amp; Get your recipe</div>
  </section>

  <!-- Row 1 / Screen: occasion selected -->
  <section class="screen" style="left:1201px;top:238px;height:504px">
    <div class="status"><span>9:41</span><svg width="44" height="8" viewBox="0 0 44 8"><rect x="0" y="5" width="2" height="3" fill="#111"/><rect x="3" y="3.5" width="2" height="4.5" fill="#111"/><rect x="6" y="2" width="2" height="6" fill="#111"/><rect x="9" y="0" width="2" height="8" fill="#111"/><path d="M16 3a6 6 0 0 1 9 0l-1 1a4.5 4.5 0 0 0-7 0zM18.5 5.5a2.5 2.5 0 0 1 4 0L20.5 8z" fill="#111"/><rect x="31" y="1" width="11" height="6" rx="1.5" fill="#111"/><rect x="42.5" y="3" width="1" height="2" fill="#111"/></svg></div>
    <div class="back"><i><svg width="6" height="8" viewBox="0 0 6 8"><path d="M4.5 1 1.5 4l3 3" stroke="#fff" stroke-width="1.4" fill="none"/></svg></i>Back</div>
    <div class="banner"><b>Generate Recipes</b><span>Lorem Ipsum is simply</span><em>✦ Surprise Me!</em></div>
    <div class="heading">Customise your recipe</div>
    <div class="tabs"><span>Add Ingredients</span><span>Cousine</span><span class="on">Occasion</span></div>
    <div class="chips" style="left:12px;top:212px"><span class="chip on">Christmas</span><span class="chip">Thanks Giving</span><span class="chip">Birthday</span><span class="chip">Marriage Anniversary</span><span class="chip">Week End</span></div>
    <div class="subbar" style="top:440px">Subscribe to add maximum cooking time<svg width="6" height="9" viewBox="0 0 6 9"><path d="M1 1l3.5 3.5L1 8" stroke="#555" fill="none"/></svg></div>
    <div class="cta" style="top:467px">Get your recipe</div>
  </section>

  <!-- Row 1 / Screen: recipe details -->
  <section class="screen" style="left:1463px;top:238px;height:566px">
    <div class="status"><span>9:41</span><svg width="44" height="8" viewBox="0 0 44 8"><rect x="0" y="5" width="2" height="3" fill="#111"/><rect x="3" y="3.5" width="2" height="4.5" fill="#111"/><rect x="6" y="2" width="2" height="6" fill="#111"/><rect x="9" y="0" width="2" height="8" fill="#111"/><path d="M16 3a6 6 0 0 1 9 0l-1 1a4.5 4.5 0 0 0-7 0zM18.5 5.5a2.5 2.5 0 0 1 4 0L20.5 8z" fill="#111"/><rect x="31" y="1" width="11" height="6" rx="1.5" fill="#111"/><rect x="42.5" y="3" width="1" height="2" fill="#111"/></svg></div>
    <div class="back"><i><svg width="6" height="8" viewBox="0 0 6 8"><path d="M4.5 1 1.5 4l3 3" stroke="#fff" stroke-width="1.4" fill="none"/></svg></i>Back</div>
    <div class="title" style="left:12px;top:72px">Recipe Details</div>
    <div class="small" style="left:12px;top:103px">Cuisine</div>
    <div style="left:12px;top:117px;font-size:7.6px;font-weight:500">Mexican Cuisine</div>
    <div class="btn line" style="left:182px;top:103px;width:38px;height:26px;font-size:7.5px">Edit</div>
    <div style="left:0;top:145px;width:233px;height:32px;background:var(--orange);color:#fff;display:flex;align-items:center;justify-content:space-between;padding:0 12px;font-size:8.5px;font-weight:500"><span>Recipe name</span><span style="display:flex;gap:4px;align-items:center;font-size:7.5px"><svg width="9" height="9" viewBox="0 0 10 10"><circle cx="5" cy="5" r="4.2" stroke="#fff" fill="none"/><path d="M5 2.5V5l1.8 1.2" stroke="#fff" fill="none"/></svg>20 min</span></div>
    <div class="label" style="left:12px;top:196px">Preparation</div>
    <p class="para" style="left:12px;top:215px">Lorem Ipsum is simply dummy text of the printing and typesetting industry. Lorem Ipsum has been the industry's standard dummy text ever since the 1500s, when an unknown printer took a galley of type and scrambled it to make a type specimen book. It has survived not only five centuries, but also the leap into electronic typesetting, remaining essentially unchanged.</p>
    <div class="label" style="left:12px;top:334px">Ingredients</div>
    <div class="list-item" style="left:12px;top:357px">Cuisine</div>
    <div class="rule" style="left:12px;top:376px"></div>
    <div class="list-item" style="left:12px;top:386px">Onion</div>
    <div class="rule" style="left:12px;top:404px"></div>
    <div class="label" style="left:12px;top:424px">Spices</div>
    <div class="list-item" style="left:12px;top:448px">Cardamom</div>
    <div class="rule" style="left:12px;top:466px"></div>
    <div class="list-item" style="left:12px;top:476px">Cinnamon</div>
    <div class="rule" style="left:12px;top:494px"></div>
    <div class="btn primary" style="left:12px;top:525px;width:100px">Get New!</div>
    <div class="btn ghost" style="left:120px;top:525px;width:100px">Save For Later</div>
  </section>

  <!-- Row 1 / Screen: subscribe prompt -->
  <section class="screen dimmed" style="left:1720px;top:238px;height:504px">
    <div style="left:0;top:118px;width:233px;height:36px;background:#6b4424;opacity:.7"></div>
    <div class="closer" style="left:107px;top:214px"><svg width="8" height="8" viewBox="0 0 8 8"><path d="M1 1l6 6M7 1 1 7" stroke="#111" stroke-width="1.4"/></svg></div>
    <div class="sheet" style="top:249px;height:255px"></div>
    <div role="img" aria-label="Illustration of a person holding a large key beside a padlock" style="left:72px;top:277px;width:90px;height:78px;border-radius:50% 50% 8px 8px;background:radial-gradient(circle at 50% 40%,#fbe1c3,#fdf5ee 70%)"></div>
    <div style="left:0;width:233px;top:372px;text-align:center;font-size:12px;font-weight:600;line-height:15px">Unlock all features!<br>Subscribe Now</div>
    <div style="left:30px;width:173px;top:407px;text-align:center;font-size:7.5px;color:#777;line-height:12px">Lorem Ipsum is simply dummy text of the printing and typesetting industry</div>
    <div class="btn primary" style="left:47px;top:448px;width:139px;height:26px">Suscribe Now</div>
  </section>

  <!-- Row 2 / Screen: eat out -->
  <section class="screen" style="left:179px;top:994px;height:503px">
    <div class="status"><span>9:41</span><svg width="44" height="8" viewBox="0 0 44 8"><rect x="0" y="5" width="2" height="3" fill="#111"/><rect x="3" y="3.5" width="2" height="4.5" fill="#111"/><rect x="6" y="2" width="2" height="6" fill="#111"/><rect x="9" y="0" width="2" height="8" fill="#111"/><path d="M16 3a6 6 0 0 1 9 0l-1 1a4.5 4.5 0 0 0-7 0zM18.5 5.5a2.5 2.5 0 0 1 4 0L20.5 8z" fill="#111"/><rect x="31" y="1" width="11" height="6" rx="1.5" fill="#111"/><rect x="42.5" y="3" width="1" height="2" fill="#111"/></svg></div>
    <div style="left:12px;top:36px;font-size:12px;font-weight:600;display:flex;align-items:center;gap:5px">Hello Mike <span role="img" aria-label="Small chef figure" style="width:9px;height:11px;background:var(--yellow);border-radius:2px"></span></div>
    <div style="left:12px;top:54px;font-size:6.8px;color:#888">What you want to cook today?</div>
    <div role="img" aria-label="User profile photo" style="left:194px;top:36px;width:25px;height:25px;border-radius:50%;background:linear-gradient(135deg,#d8d8d8,#555)"></div>
    <div class="field" style="left:12px;top:78px;width:208px;height:24px;background:#fff;color:#888;justify-content:space-between;padding-right:8px"><span>◎ Zip code 12345</span><svg width="6" height="9" viewBox="0 0 6 9"><path d="M1 1l3.5 3.5L1 8" stroke="#555" fill="none"/></svg></div>
    <div style="left:12px;top:115px;font-size:11.5px;font-weight:500;line-height:14px">Let’s get you a place<br>to eat</div>
    <div class="btn line" style="left:166px;top:115px;width:54px;height:24px;gap:5px;font-size:8px">Filter <svg width="9" height="7" viewBox="0 0 9 7"><path d="M0 1h9M1.5 3.5h6M3 6h3" stroke="#333"/></svg></div>
    <div style="left:26px;top:404px;width:180px;height:30px;background:#2d2d2d;border-radius:12px"></div>
    <div style="left:19px;top:398px;width:194px;height:30px;background:#3a3a3a;border-radius:12px"></div>
    <div role="img" aria-label="Restaurant photo of a cook tossing food in a flaming pan" style="left:12px;top:162px;width:208px;height:255px;border-radius:12px;background:linear-gradient(160deg,#5d5a55 0%,#8a6a4a 35%,#c0673a 60%,#3a2a20 85%)"></div>
    <div style="left:24px;top:366px;font-size:6px;color:#fff">◷ 30 min</div>
    <div style="left:24px;top:380px;font-size:8px;color:#fff;font-weight:500">The Maple Hearth</div>
    <div style="left:24px;top:394px;font-size:6.5px;color:#ddd">Burger | American Cuisine</div>
    <div style="left:178px;top:381px;width:29px;height:15px;background:var(--yellow);border-radius:3px;font-size:7px;display:flex;align-items:center;justify-content:center">4.1 ★</div>
    <div class="btn primary" style="left:12px;top:460px;width:100px;height:26px">Next</div>
    <div class="btn ghost" style="left:120px;top:460px;width:100px;height:26px">Save For Later</div>
  </section>

  <!-- Row 2 / Screen: filter sheet -->
  <section class="screen dimmed" style="left:437px;top:994px;height:503px">
    <div style="left:12px;top:160px;width:208px;height:90px;background:#2f2f2f;border-radius:12px"></div>
    <div class="closer" style="left:107px;top:220px"><svg width="8" height="8" viewBox="0 0 8 8"><path d="M1 1l6 6M7 1 1 7" stroke="#111" stroke-width="1.4"/></svg></div>
    <div class="sheet" style="top:254px;height:249px"></div>
    <div style="left:12px;top:278px;font-size:8px">Choose meal type</div>
    <div class="chip fill" style="left:12px;top:297px;width:60px;height:26px;border-radius:13px">Cuisine</div>
    <div class="chip" style="left:77px;top:297px;width:60px;height:26px;border-radius:13px;justify-content:center">Occasion</div>
    <div style="left:12px;top:340px;font-size:8px">Max distance</div>
    <div class="track" style="left:12px;top:366px"></div>
    <div style="left:12px;top:366px;width:48px;height:2px;background:var(--orange)"></div>
    <div class="knob" style="left:43px;top:357px">5m</div>
    <div style="left:12px;top:377px;font-size:7.5px;color:#666">2m</div>
    <div style="left:202px;top:377px;font-size:7.5px;color:#666">30m</div>
    <div style="left:12px;top:404px;font-size:8px">Price range</div>
    <div class="track" style="left:12px;top:429px"></div>
    <div style="left:22px;top:429px;width:52px;height:2px;background:var(--orange)"></div>
    <div class="knob" style="left:12px;top:420px">$0</div>
    <div class="knob" style="left:63px;top:420px">$25</div>
    <div style="left:0;top:467px;width:233px;height:36px;background:#2a2a2a;color:#fff;font-size:7.5px;display:flex;align-items:center;justify-content:space-between;padding:0 12px 0 10px">Subscribe to apply filter<svg width="6" height="9" viewBox="0 0 6 9"><path d="M1 1l3.5 3.5L1 8" stroke="#aaa" fill="none"/></svg></div>
  </section>

  <!-- Row 2 / Screen: meal plan with ingredients -->
  <section class="screen" style="left:694px;top:994px;height:503px">
    <div class="status"><span>9:41</span><svg width="44" height="8" viewBox="0 0 44 8"><rect x="0" y="5" width="2" height="3" fill="#111"/><rect x="3" y="3.5" width="2" height="4.5" fill="#111"/><rect x="6" y="2" width="2" height="6" fill="#111"/><rect x="9" y="0" width="2" height="8" fill="#111"/><path d="M16 3a6 6 0 0 1 9 0l-1 1a4.5 4.5 0 0 0-7 0zM18.5 5.5a2.5 2.5 0 0 1 4 0L20.5 8z" fill="#111"/><rect x="31" y="1" width="11" height="6" rx="1.5" fill="#111"/><rect x="42.5" y="3" width="1" height="2" fill="#111"/></svg></div>
    <div class="back"><i><svg width="6" height="8" viewBox="0 0 6 8"><path d="M4.5 1 1.5 4l3 3" stroke="#fff" stroke-width="1.4" fill="none"/></svg></i>Back</div>
    <div class="title" style="left:12px;top:71px">Let’s make a meal plan</div>
    <div style="left:12px;top:108px;font-size:7.5px;font-weight:500">Meal plan duration</div>
    <div class="chip" style="left:12px;top:127px;width:65px;height:26px;border-radius:13px;justify-content:center">2 days</div>
    <div class="chip fill" style="left:83px;top:127px;width:65px;height:26px;border-radius:13px">3 days</div>
    <div class="chip" style="left:154px;top:127px;width:65px;height:26px;border-radius:13px;justify-content:center">5 days</div>
    <div style="left:12px;top:173px;font-size:7.5px;font-weight:500">Do you have ingredients?</div>
    <div class="radio" style="left:12px;top:194px"><i class="on"></i>Yes</div>
    <div class="radio" style="left:69px;top:194px"><i></i>No</div>
    <div style="left:12px;top:226px;font-size:7.5px;font-weight:500">Add your ingredients</div>
    <div class="field" style="left:12px;top:248px;width:155px">Enter ingredient name</div>
    <div class="add" style="left:170px;top:248px">Add +</div>
    <div class="chips" style="left:12px;top:288px"><span class="chip x">Beef</span><span class="chip x">Onion</span><span class="chip x">Tomatoes</span><span class="chip x">Garlic</span><span class="chip x">Chili</span></div>
    <div class="subbar" style="top:439px">Subscribe to maximise your meal plan<svg width="6" height="9" viewBox="0 0 6 9"><path d="M1 1l3.5 3.5L1 8" stroke="#555" fill="none"/></svg></div>
    <div class="cta" style="top:466px">Get your meal plan</div>
  </section>

  <!-- Row 2 / Screen: meal plan without ingredients -->
  <section class="screen" style="left:951px;top:994px;height:503px">
    <div class="status"><span>9:41</span><svg width="44" height="8" viewBox="0 0 44 8"><rect x="0" y="5" width="2" height="3" fill="#111"/><rect x="3" y="3.5" width="2" height="4.5" fill="#111"/><rect x="6" y="2" width="2" height="6" fill="#111"/><rect x="9" y="0" width="2" height="8" fill="#111"/><path d="M16 3a6 6 0 0 1 9 0l-1 1a4.5 4.5 0 0 0-7 0zM18.5 5.5a2.5 2.5 0 0 1 4 0L20.5 8z" fill="#111"/><rect x="31" y="1" width="11" height="6" rx="1.5" fill="#111"/><rect x="42.5" y="3" width="1" height="2" fill="#111"/></svg></div>
    <div class="back"><i><svg width="6" height="8" viewBox="0 0 6 8"><path d="M4.5 1 1.5 4l3 3" stroke="#fff" stroke-width="1.4" fill="none"/></svg></i>Back</div>
    <div class="title" style="left:12px;top:71px">Let’s make a meal plan</div>
    <div style="left:12px;top:108px;font-size:7.5px;font-weight:500">Meal plan duration</div>
    <div class="chip" style="left:12px;top:127px;width:65px;height:26px;border-radius:13px;justify-content:center">2 days</div>
    <div class="chip fill" style="left:83px;top:127px;width:65px;height:26px;border-radius:13px">3 days</div>
    <div class="chip" style="left:154px;top:127px;width:65px;height:26px;border-radius:13px;justify-content:center">5 days</div>
    <div style="left:12px;top:173px;font-size:7.5px;font-weight:500">Do you have ingredients?</div>
    <div class="radio" style="left:12px;top:194px"><i></i>Yes</div>
    <div class="radio" style="left:69px;top:194px"><i class="on"></i>No</div>
    <div class="btn line" style="left:12px;top:225px;width:127px;height:26px;font-size:7.5px;font-weight:500">Generate Ingredients</div>
    <div class="subbar" style="top:439px">Subscribe to maximise your meal plan<svg width="6" height="9" viewBox="0 0 6 9"><path d="M1 1l3.5 3.5L1 8" stroke="#555" fill="none"/></svg></div>
    <div class="cta" style="top:466px">Get your meal plan</div>
  </section>

  <!-- Row 2 / Screen: recipe card -->
  <section class="screen" style="left:1217px;top:994px;height:503px">
    <div class="status"><span>9:41</span><svg width="44" height="8" viewBox="0 0 44 8"><rect x="0" y="5" width="2" height="3" fill="#111"/><rect x="3" y="3.5" width="2" height="4.5" fill="#111"/><rect x="6" y="2" width="2" height="6" fill="#111"/><rect x="9" y="0" width="2" height="8" fill="#111"/><path d="M16 3a6 6 0 0 1 9 0l-1 1a4.5 4.5 0 0 0-7 0zM18.5 5.5a2.5 2.5 0 0 1 4 0L20.5 8z" fill="#111"/><rect x="31" y="1" width="11" height="6" rx="1.5" fill="#111"/><rect x="42.5" y="3" width="1" height="2" fill="#111"/></svg></div>
    <div style="left:12px;top:42px;width:208px;height:385px;background:#f8f8f8;border-radius:10px"></div>
    <div style="left:12px;top:42px;width:208px;height:34px;background:var(--orange);border-radius:10px 10px 0 0;color:#fff;display:flex;align-items:center;justify-content:space-between;padding:0 10px;font-size:8.5px;font-weight:500"><span>Recipe name</span><span style="display:flex;gap:4px;align-items:center;font-size:7.5px"><svg width="9" height="9" viewBox="0 0 10 10"><circle cx="5" cy="5" r="4.2" stroke="#fff" fill="none"/><path d="M5 2.5V5l1.8 1.2" stroke="#fff" fill="none"/></svg>20 min</span></div>
    <div class="label" style="left:22px;top:96px">Preparation</div>
    <p class="para" style="left:22px;top:114px;width:190px">Lorem Ipsum is simply dummy text of the printing and typesetting industry. Lorem Ipsum has been the industry's standard dummy text ever since the 1500s, when an unknown printer took a galley of type and scrambled it to make a type specimen book. It has survived not only five centuries, but also the leap into electronic typesetting, remaining essentially unchanged.</p>
    <div class="label" style="left:22px;top:232px">Ingredients</div>
    <div class="list-item" style="left:22px;top:251px">Cuisine</div>
    <div class="rule" style="left:22px;top:269px;width:188px"></div>
    <div class="list-item" style="left:22px;top:280px">Onion</div>
    <div class="label" style="left:22px;top:308px">Spices</div>
    <div class="list-item" style="left:22px;top:328px">Cardamom</div>
    <div class="rule" style="left:22px;top:346px;width:188px"></div>
    <div class="list-item" style="left:22px;top:356px">Cinnamon</div>
    <div class="btn line" style="left:22px;top:388px;width:188px;height:27px">Edit</div>
    <div class="btn primary" style="left:12px;top:460px;width:100px;height:26px">Get New!</div>
    <div class="btn ghost" style="left:120px;top:460px;width:100px;height:26px">Save For Later</div>
  </section>

  <!-- Row 2 / Screen: navigation drawer -->
  <section class="screen" style="left:1475px;top:994px;width:232px;height:503px">
    <div style="left:210px;top:0;width:22px;height:503px;background:linear-gradient(#3a2a1e,#6a4a30 50%,#2f2a26)"></div>
    <div role="img" aria-label="User profile photo" style="left:12px;top:24px;width:25px;height:25px;border-radius:50%;background:linear-gradient(135deg,#d8d8d8,#555)"></div>
    <div style="left:46px;top:24px;font-size:12px;font-weight:600;display:flex;align-items:center;gap:5px">Hello Mike <span role="img" aria-label="Small chef figure" style="width:9px;height:11px;background:var(--yellow);border-radius:2px"></span></div>
    <div style="left:46px;top:42px;font-size:6.8px;color:#888">Lorem Ipsum is simply dummy</div>
    <div style="left:180px;top:26px;width:16px;height:16px;border-radius:50%;background:#111;display:flex;align-items:center;justify-content:center"><svg width="7" height="7" viewBox="0 0 8 8"><path d="M1 1l6 6M7 1 1 7" stroke="#fff" stroke-width="1.4"/></svg></div>
    <div class="rule" style="left:0;top:68px;width:210px"></div>
    <nav class="menu">
      <div><svg width="11" height="11" viewBox="0 0 12 12"><path d="M1.5 5.5 6 1.5l4.5 4V10.5h-9z" stroke="#222" fill="none"/></svg>Home</div>
      <div><svg width="11" height="11" viewBox="0 0 12 12"><rect x="1.5" y="1.5" width="9" height="9" rx="2" stroke="#222" fill="none"/><path d="M4 5h4M4 7.5h3" stroke="#222"/></svg>Recipe</div>
      <div><svg width="11" height="11" viewBox="0 0 12 12"><rect x="1.5" y="1" width="9" height="10" rx="1" stroke="#222" fill="none"/><path d="M4 4h4M4 6h4M4 8h4" stroke="#222"/></svg>Restaurant</div>
      <div><svg width="11" height="11" viewBox="0 0 12 12"><path d="M2 1.5l8 9M10 1.5l-8 9" stroke="#222"/></svg>Meal</div>
      <div><svg width="11" height="11" viewBox="0 0 12 12"><circle cx="4" cy="4" r="1.8" stroke="#222" fill="none"/><circle cx="8.5" cy="4" r="1.8" stroke="#222" fill="none"/><path d="M1 10c0-2 6-2 6 0M5.5 10c0-2 6-2 6 0" stroke="#222" fill="none"/></svg>Community</div>
      <div><svg width="11" height="11" viewBox="0 0 12 12"><circle cx="6" cy="6" r="5" stroke="#222" fill="none"/><circle cx="6" cy="5" r="1.8" stroke="#222" fill="none"/><path d="M3 9.5c1.5-2 4.5-2 6 0" stroke="#222" fill="none"/></svg>Profile</div>
    </nav>
    <div style="left:12px;top:410px;width:186px;height:82px;background:var(--yellow-pale);border-radius:8px"></div>
    <div style="left:24px;top:426px;font-size:7.5px;font-weight:600">Start Your 30 Days Free Trail</div>
    <div style="left:24px;top:441px;font-size:6px;color:#999">Lorem Ipsum is simply dummy text of</div>
    <div style="left:24px;top:459px;width:82px;height:17px;background:var(--yellow);border-radius:3px;font-size:6.5px;font-weight:500;display:flex;align-items:center;justify-content:center">Get Premium Plan</div>
    <div role="img" aria-label="Illustration of a chef carrying a covered dish" style="left:150px;top:400px;width:46px;height:92px;border-radius:20px 20px 4px 4px;background:linear-gradient(#f8cf3a,#fae287 60%,#fdf2cf)"></div>
  </section>
</div>
</body>
</html>
```